Corporate Branding - Web and Print

A UK based company will like to use an existing logo to create branding materials for all marketing related documents, including business card, prints, letterhead, Website, Twitter, Facebook, Instagram logo etc. This company serves high-end clientele in the fashion, health and wellness and as such high quality and class is of utmost importance.
Where the logo can be modernised without losing its character then experiment. The main thing is to have a corporate branding which can be used later for brochures, Business Plan infographics.
The prominent colour within the organisation is burnt orange with no secondary colour. However if you believe a secondary colour is needed then use it, otherwise keep it simple and classy. Any chosen colours have to match perfectly.
Target Market(s)
High net worth individuals
Industry/Entity Type
Health And Wellness
Contact Information for Business Card
classy

```html
<!DOCTYPE html>
<html lang="en">
<head>
<meta charset="utf-8">
<title>Velmora Business Card</title>
<link href="https://fonts.googleapis.com/css2?family=Open+Sans:wght@400;600;700;800&display=swap" rel="stylesheet">
<style>
  :root {
    --backdrop: #e9e4df;
    --card: #1f2a35;
    --accent: #fbbd2a;
    --ink-light: #f4f4f4;
  }
  * { margin: 0; padding: 0; box-sizing: border-box; }
  html, body {
    width: 1200px; height: 900px; overflow: hidden;
    background: var(--backdrop);
    font-family: "Open Sans", Arial, sans-serif;
  }
  .canvas { position: relative; width: 1200px; height: 900px; }
  .card {
    position: absolute;
    background: var(--card);
    box-shadow: 0 8px 24px rgba(0,0,0,0.25);
  }
  .card--front { left: 238px; top: 63px; width: 555px; height: 343px; }
  .card--back { left: 457px; top: 518px; width: 560px; height: 342px; }

  .brand-mark {
    position: absolute;
    display: flex; flex-direction: column; align-items: center;
  }
  .brand-mark__dot { border-radius: 50%; background: var(--accent); }
  .brand-mark__name { color: var(--accent); font-weight: 800; letter-spacing: 0.04em; line-height: 1; }

  .card--front .brand-mark { left: 50px; top: 88px; width: 200px; }
  .card--front .brand-mark__dot { width: 116px; height: 116px; margin-bottom: 14px; }
  .card--front .brand-mark__name { font-size: 30px; }

  .card--back .brand-mark { left: 0; top: 95px; width: 560px; }
  .card--back .brand-mark__dot { width: 80px; height: 80px; margin-bottom: 18px; }
  .card--back .brand-mark__name { font-size: 48px; }

  .holder { position: absolute; left: 302px; top: 64px; color: var(--ink-light); }
  .holder__name { color: var(--accent); font-weight: 700; font-size: 20px; line-height: 26px; }
  .holder__title { font-size: 14.5px; line-height: 18px; }
  .holder__address { margin-top: 22px; font-size: 14.5px; line-height: 17px; }
  .contacts { margin-top: 18px; list-style: none; }
  .contacts li { display: flex; align-items: center; font-size: 14.5px; height: 23px; }
  .contacts svg { width: 12px; height: 12px; margin: 0 11px 0 2px; fill: var(--accent); flex: none; }
</style>
</head>
<body>
<main class="canvas">
  <section class="card card--front">
    <div class="brand-mark">
      <span class="brand-mark__dot"></span>
      <span class="brand-mark__name">VELMORA</span>
    </div>
    <div class="holder">
      <p class="holder__name">Adrian Hale</p>
      <p class="holder__title">Managing Director</p>
      <p class="holder__address">48 Carlow Street, Camden<br>London, NW1 7HT</p>
      <ul class="contacts">
        <li><svg viewBox="0 0 24 24"><path d="M6.6 10.8a15.1 15.1 0 0 0 6.6 6.6l2.2-2.2a1 1 0 0 1 1-.25 11.4 11.4 0 0 0 3.6.57 1 1 0 0 1 1 1V20a1 1 0 0 1-1 1A17 17 0 0 1 3 4a1 1 0 0 1 1-1h3.5a1 1 0 0 1 1 1c0 1.25.2 2.45.57 3.57a1 1 0 0 1-.25 1z"/></svg>(020)-318-5527</li>
        <li><svg viewBox="0 0 24 24"><path d="M7 1h10a2 2 0 0 1 2 2v18a2 2 0 0 1-2 2H7a2 2 0 0 1-2-2V3a2 2 0 0 1 2-2zm0 3v14h10V4zm5 15.5a1 1 0 1 0 0 2 1 1 0 0 0 0-2z"/></svg>077-902-4413</li>
        <li><svg viewBox="0 0 24 24"><path d="M2 4h20v16H2zm2 2v.5l8 5 8-5V6zm0 2.9V18h16V8.9l-8 5z"/></svg>hello@velmora.co.uk</li>
        <li><svg viewBox="0 0 24 24"><path d="M12 2a10 10 0 1 0 0 20 10 10 0 0 0 0-20zm-1 17.9A8 8 0 0 1 4.2 10.2L9 15v1a2 2 0 0 0 2 2zm6.9-2.5A2 2 0 0 0 16 16h-1v-3a1 1 0 0 0-1-1H8v-2h2a1 1 0 0 0 1-1V7h2a2 2 0 0 0 2-2v-.4a8 8 0 0 1 2.9 12.8z"/></svg>www.velmora.co.uk</li>
      </ul>
    </div>
  </section>

  <section class="card card--back">
    <div class="brand-mark">
      <span class="brand-mark__dot"></span>
      <span class="brand-mark__name">VELMORA</span>
    </div>
  </section>
</main>
</body>
</html>
```